Front Cover Page and Back Cover for Biography Book

Create a book front cover page and back cover for the biography book called Beyond the Tide: The Long Road of Pham Quoc Lanh
Blurb/Summary:
Step into the extraordinary life of Pham Quoc Lanh in Beyond the Tide: The Long Road of Pham Quoc Lanh, a gripping memoir of resilience, determination, and triumph. Born in Quang Ngai, Vietnam, in 1938, Lanh grew up amid the unrelenting challenges of famine, war, and poverty. Yet, his unshakable thirst for education and self-improvement became the foundation of a journey that would defy every expectation.
From studying under flickering oil lamps in hidden village schools during the resistance against French colonial rule to enduring the hardships of the Vietnam War, Lanh’s story is set against the dramatic backdrop of a nation in turmoil. Despite familial and societal obstacles, his passion for knowledge drove him to excel academically and chart a future far beyond the limitations of his humble beginnings.
As a Navy officer, Lanh balanced the rigours of military life with an entrepreneurial spirit that saw him transform his circumstances. Whether selling ice cream, expanding a fleet of fishing boats, or salvaging a sunken ship to create a thriving business, his ingenuity and drive turned adversity into opportunity. Along the way, he navigated personal sacrifices, betrayal, and daring escapes as Vietnam descended into chaos, all while keeping his family at the heart of his efforts.
Through the lens of Lanh’s incredible life, Beyond the Tide highlights the power of education, perseverance, and community in overcoming the impossible. This memoir is not just a story of survival but a testament to human strength, offering readers an inspiring tale of hope, legacy, and the relentless pursuit of a better life. Perfect for those seeking an uplifting narrative with historical and emotional depth, this is a book that will stay with you long after the final page.
Please find the full book attached.
Photos of lanh can be found here in the photo album: https://albums.pictoria-share.example/Xk7RmqTz2wLpYc9Vn

```html
<!DOCTYPE html>
<html lang="en">
<head>
<meta charset="utf-8">
<title>Beyond the Tide: The Long Road of Pham Quoc Lanh — Cover Spread</title>
<link rel="stylesheet" href="https://fonts.googleapis.com/css2?family=Saira+Extra+Condensed:wght@300;700&family=Open+Sans:wght@300;400&display=swap">
<style>
  :root {
    --backdrop: #c9cacc;
    --ink-dark: #0c0f15;
    --paper: #ebe9e1;
    --title-dark: #2f3433;
    --teal: #86b8c3;
    --white: #ffffff;
    --body-ink: #3a3d3c;
    --photo-shadow: #141a24;
    --photo-mid: #6f7886;
  }
  * { margin: 0; padding: 0; box-sizing: border-box; }
  html, body { width: 889px; height: 1200px; overflow: hidden; background: var(--backdrop); }
  .canvas { position: relative; width: 889px; height: 1200px; }

  .spread {
    position: absolute; left: 20px; top: 272px;
    width: 849px; height: 655px; overflow: hidden;
    background: var(--ink-dark);
  }

  .back-field {
    position: absolute; left: 0; top: 0; width: 441px; height: 655px;
    background:
      radial-gradient(ellipse 62% 58% at 50% 52%, var(--paper) 55%, rgba(235,233,225,0) 100%),
      radial-gradient(ellipse 90% 80% at 50% 50%, #d8d6cf 40%, var(--ink-dark) 100%);
  }
  .seam { position: absolute; left: 441px; top: 0; width: 1px; height: 655px; background: rgba(255,255,255,0.25); }

  .front-field {
    position: absolute; left: 442px; top: 0; width: 407px; height: 655px;
    background:
      radial-gradient(ellipse 55% 42% at 60% 32%, rgba(230,231,234,0.85) 30%, rgba(12,15,21,0) 100%),
      var(--ink-dark);
  }
  .portrait {
    position: absolute; left: 120px; top: 50px; width: 270px; height: 420px;
    border-radius: 46% 46% 20% 20%;
    background:
      radial-gradient(ellipse 38% 26% at 45% 28%, #8a6a58 0%, rgba(138,106,88,0) 100%),
      radial-gradient(ellipse 70% 45% at 55% 80%, var(--photo-mid) 0%, var(--photo-shadow) 90%);
    filter: blur(2px);
  }

  .blurb {
    position: absolute; left: 78px; top: 187px; width: 254px;
    font-family: "Open Sans", sans-serif; font-weight: 300;
    font-size: 8.4px; line-height: 11.5px; color: var(--body-ink);
    text-align: justify;
  }
  .blurb p + p { margin-top: 6px; }

  .type-layer { position: absolute; left: 0; top: 0; width: 849px; height: 655px; overflow: hidden; }
  .type-layer text { font-family: "Saira Extra Condensed", "Arial Narrow", sans-serif; text-transform: uppercase; }
  .kicker { font-weight: 300; }
  .main { font-weight: 700; }
  .ink-dark { fill: var(--title-dark); }
  .ink-white { fill: var(--white); }
  .ink-teal { fill: var(--teal); }
  .type-layer .author-line { font-family: "Open Sans", sans-serif; font-weight: 400; }
</style>
</head>
<body>
<main class="canvas">
  <section class="spread">
    <div class="back-field"></div>
    <div class="seam"></div>
    <div class="front-field">
      <div class="portrait" role="img" aria-label="Portrait photograph of Pham Quoc Lanh in a grey suit and blue dotted tie, softly vignetted"></div>
    </div>

    <div class="blurb">
      <p>Step into the extraordinary life of Pham Quoc Lanh in Beyond the Tide: The Long Road of Pham Quoc Lanh, a gripping memoir of resilience, determination, and triumph. Born in Quang Ngai, Vietnam, in 1938, Lanh grew up amid the unrelenting challenges of famine, war, and poverty. Yet, his unshakable thirst for education and self-improvement became the foundation of a journey that would defy every expectation.</p>
      <p>From studying under flickering oil lamps in hidden village schools during the resistance against French colonial rule to enduring the hardships of the Vietnam War, Lanh’s story is set against the dramatic backdrop of a nation in turmoil. Despite familial and societal obstacles, his passion for knowledge drove him to excel academically and chart a future far beyond the limitations of his humble beginnings.</p>
      <p>As a Navy officer, Lanh balanced the rigours of military life with an entrepreneurial spirit that saw him transform his circumstances. Whether selling ice cream, expanding a fleet of fishing boats, or salvaging a sunken ship to create a thriving business, his ingenuity and drive turned adversity into opportunity. Along the way, he navigated personal sacrifices, betrayal, and daring escapes as Vietnam descended into chaos, all while keeping his family at the heart of his efforts.</p>
      <p>Through the lens of Lanh’s incredible life, Beyond the Tide highlights the power of education, perseverance, and community in overcoming the impossible. This memoir is not just a story of survival but a testament to human strength, offering readers an inspiring tale of hope, legacy, and the relentless pursuit of a better life. Perfect for those seeking an uplifting narrative with historical and emotional depth, this is a book that will stay with you long after the final page.</p>
    </div>

    <svg class="type-layer" viewBox="0 0 849 655" width="849" height="655">
      <!-- Back cover title -->
      <g class="back-title">
        <text class="kicker ink-dark" x="112" y="77" font-size="36" textLength="186" lengthAdjust="spacingAndGlyphs">Beyond the Tide:</text>
        <text class="main ink-dark" x="78" y="117" font-size="50" textLength="255" lengthAdjust="spacingAndGlyphs">The Long Road</text>
        <text class="main ink-dark" x="78" y="158" font-size="50" textLength="255" lengthAdjust="spacingAndGlyphs">of Pham Quoc Lanh</text>
      </g>

      <!-- Spine -->
      <g class="spine">
        <text class="ink-dark" transform="translate(418,63) rotate(90)" font-size="15" textLength="335" lengthAdjust="spacingAndGlyphs"><tspan class="kicker">Beyond the Tide: </tspan><tspan class="main">The Long Road of Pham Quoc Lanh</tspan></text>
        <text class="author-line ink-dark" transform="translate(421,504) rotate(90)" font-size="7" textLength="80" lengthAdjust="spacing">AUTHOR NAME</text>
      </g>

      <!-- Front cover title -->
      <g class="front-title" transform="translate(442,0)">
        <text class="kicker ink-white" x="84" y="494" font-size="44" textLength="252" lengthAdjust="spacingAndGlyphs">Beyond the Tide:</text>
        <text class="main ink-teal" x="37" y="555" font-size="64" textLength="334" lengthAdjust="spacingAndGlyphs">The Long Road</text>
        <text class="main ink-teal" x="37" y="611" font-size="64" textLength="334" lengthAdjust="spacingAndGlyphs">of Pham Quoc Lanh</text>
        <text class="author-line ink-white" x="162" y="630" font-size="8" textLength="92" lengthAdjust="spacing">AUTHOR NAME</text>
      </g>
    </svg>
  </section>
</main>
</body>
</html>
```